New Business Tri Fold Brochure

Tri Fold Brochure for new business. I have attached a few versions of our logo and would like the color scheme to be the blue and grey colors from the logo. I have also attached examples of the data that I would like implemented into the brochure such as the FAQ's and general company information. I would like the 3 general points (hassle free, save money, no risk guarantee) to be matched to appropriate icons. I also need the 3 steps for "how it works" matched to appropriate themed icons. I would like the back of the brochure to have a photo of our building, map of location and all contact information. Address: 728 W. Brindle Crest Ave Suite 410 Fort Lauderdale FL 33417. Phone- 754-618-2094. Email: info@harbor-tallyworks.com. Website: www.harbor-tallyworks.com

```html
<!DOCTYPE html>
<html lang="en">
<head>
<meta charset="utf-8">
<title>Harbor Tallyworks – Tri Fold Brochure (Inside)</title>
<link rel="stylesheet" href="https://fonts.googleapis.com/css2?family=Roboto+Condensed:wght@700&family=Source+Sans+3:wght@400&family=Arimo:wght@400&display=swap">
<style>
  :root {
    --brand-blue: #2a78c2;
    --brand-blue-deep: #1f6bb6;
    --brand-grey: #7d7f83;
    --paper: #f7f7f7;
    --panel-mid-top: #e9e9e9;
    --panel-mid-bottom: #f1f1f1;
    --band-grey: #d6d6d6;
    --band-grey-mid: #c9c9c9;
    --icon-disc: #e6e6e6;
    --backdrop: #8ec8e7;
  }
  * { box-sizing: border-box; margin: 0; padding: 0; }
  html, body { width: 1200px; height: 892px; overflow: hidden; }
  body { background: var(--backdrop); position: relative; }

  .brochure {
    position: absolute; left: 30px; top: 41px;
    width: 1140px; height: 810px;
    background: var(--paper);
    display: flex;
    box-shadow: 0 6px 22px rgba(0,40,80,.18);
  }
  .panel { position: relative; width: 380px; height: 100%; }
  .panel--middle {
    background: linear-gradient(180deg, var(--panel-mid-top), var(--panel-mid-bottom) 85%);
    border-left: 1px solid #dcdcdc; border-right: 1px solid #dcdcdc;
  }

  .footer-band {
    position: absolute; left: 0; right: 0; top: 651px; height: 127px;
    background: var(--band-grey);
  }
  .panel--middle .footer-band { background: var(--band-grey-mid); }
  .footer-rule {
    position: absolute; left: 0; right: 0; top: 784px; height: 26px;
    background: var(--brand-blue-deep);
  }

  .feature { position: absolute; left: 0; width: 380px; }
  .feature__icon {
    position: absolute; width: 110px; height: 110px; border-radius: 50%;
    background: var(--icon-disc);
  }
  .feature__icon::after {
    content: ""; position: absolute; left: 28px; top: 28px;
    width: 54px; height: 54px; border-radius: 12px;
    background: var(--brand-blue); opacity: .85;
  }
  .feature__icon--seal::after { border-radius: 50%; left: 13px; top: 13px; width: 84px; height: 84px; }
  .feature__title {
    position: absolute; font: 700 17.5px/1 "Roboto Condensed", sans-serif;
    color: var(--brand-blue);
  }
  .feature__text {
    position: absolute; font: 400 14.3px/18px "Source Sans 3", sans-serif;
    color: var(--brand-blue);
  }

  .left .feature__icon { left: 58px; }
  .left .feature__title { left: 168px; }
  .left .feature__text { left: 168px; width: 195px; }

  .right .feature__icon { left: 40px; }
  .right .feature__title { left: 148px; }
  .right .feature__text { left: 148px; width: 200px; }

  .section-heading {
    position: absolute; font: 700 17px/1 "Roboto Condensed", sans-serif;
    color: var(--brand-blue); letter-spacing: .2px;
  }
  .copy {
    position: absolute; left: 31px; width: 325px;
    font: 400 14.6px/24.4px "Arimo", sans-serif; color: var(--brand-blue);
  }

  .brand {
    position: absolute; left: 0; right: 0; top: 678px;
    display: flex; flex-direction: column; align-items: center; gap: 8px;
  }
  .brand__dot { width: 34px; height: 34px; border-radius: 50%; background: var(--brand-blue); }
  .brand__name {
    font: 700 22px/1 "Roboto Condensed", sans-serif; color: var(--brand-blue);
    letter-spacing: 1px;
  }
</style>
</head>
<body>
  <main class="brochure">
    <section class="panel left">
      <div class="feature" style="top:0">
        <div class="feature__icon" style="top:114px" role="img" aria-label="Icon of a business owner working at a laptop"></div>
        <h3 class="feature__title" style="top:123px">Hassle Free</h3>
        <p class="feature__text" style="top:148px">you are busy running a business; let's negotiate for you and put money back in your pocket!</p>
      </div>
      <div class="feature" style="top:0">
        <div class="feature__icon" style="top:304px" role="img" aria-label="Icon of a piggy bank with a dollar coin"></div>
        <h3 class="feature__title" style="top:313px">Save Money</h3>
        <p class="feature__text" style="top:338px">We save business owners and average $500 per month.</p>
      </div>
      <div class="feature" style="top:0">
        <div class="feature__icon feature__icon--seal" style="top:495px" role="img" aria-label="Guarantee seal"></div>
        <h3 class="feature__title" style="top:503px">No Risk Guarantee</h3>
        <p class="feature__text" style="top:528px">We guarantee we will lower your bill or there is no charge for our service!</p>
      </div>
      <div class="footer-band"></div>
      <div class="footer-rule"></div>
    </section>

    <section class="panel panel--middle">
      <h2 class="section-heading" style="left:31px;top:67px">WHO WE ARE.</h2>
      <p class="copy" style="top:93px">Harbor Tallyworks is a company that was founded by previous merchant processing professionals with over 20 years of industry knowledge and experience. We know all of the tricks that the big companies use to fill their pockets with your money! we use that industry knowledge to negotiate and save your business money.</p>
      <h2 class="section-heading" style="left:31px;top:317px">WHAT WE DO.</h2>
      <p class="copy" style="top:344px">Once you sign up, how our experts get to work negotiating with your current merchant processing provider. Our goal is to get you the the lowest rates possible without changing providers for having to get expensive new equipment. We offer a no risk savings guarantee. If we can't save you money; you don't pay us a dime!<br>100% risk free.</p>
      <div class="footer-band"></div>
      <div class="brand">
        <span class="brand__dot"></span>
        <span class="brand__name">HARBOR TALLYWORKS</span>
      </div>
      <div class="footer-rule"></div>
    </section>

    <section class="panel right">
      <h2 class="section-heading" style="left:121px;top:63px">HOW IT WORKS</h2>
      <div class="feature" style="top:0">
        <div class="feature__icon" style="top:119px" role="img" aria-label="Icon of a hand signing with a pen"></div>
        <h3 class="feature__title" style="top:128px">Sign up</h3>
        <p class="feature__text" style="top:153px">Provide some basic information and copy of your most recent statement for invoice</p>
      </div>
      <div class="feature" style="top:0">
        <div class="feature__icon" style="top:299px" role="img" aria-label="Icon of an agent on the phone"></div>
        <h3 class="feature__title" style="top:308px">We contact your provider</h3>
        <p class="feature__text" style="top:333px">Our experts get to work negotiating with your current provider on your behalf for the lowest rates possible</p>
      </div>
      <div class="feature" style="top:0">
        <div class="feature__icon" style="top:488px" role="img" aria-label="Icon of a wallet with banknotes"></div>
        <h3 class="feature__title" style="top:497px">You save money</h3>
        <p class="feature__text" style="top:522px">Your monthly fees get reduced and you save money we split the savings for the first year and the rest goes into your wallet simple!</p>
      </div>
      <div class="footer-band"></div>
      <div class="footer-rule"></div>
    </section>
  </main>
</body>
</html>
```